DL Flyer,A4 letterhead, with compliments slip, and envelopes
For new safety consultancy business
DL Flyer,A4 letterhead, with compliments slip, and envelopes - Consulting
Creative Brief
Yes
New safety consultancy in Australia, focussing on small to medium industrial businesses.
Modern
Unsure - similar to logo maybe?
DL size FLYER TO be one sided glossy to INCLUDE FOLLOWING WORDS:
Occupational Health and Safety is a minefield of laws and regulations for the unprepared employer. Did you know that no matter how small an employer you are, by law you still need a safety management system? Did you know that you need specific procedures in place to prove that your employees, contractors and visitors are safe?
Let Hazardwell implement an OHS strategy that is cost effective and right for you.
Our services not only include OHS advice but also the development of:
- OHS management systems
- Risk assessments
- Safe work method statements
- Checklists, forms and registers
- Training and toolbox talks
Hazardwell is a local business, accredited in auditing Australian Standard 4801 OHS management systems. To arrange a free OHS pulse check of your systems and find out if you meet legislation, call Hazardwell now on 0418 264 907.
info@hazardwellexample.com.au
www.hazardwellexample.com.au
LETTER HEAD TO INCLUDE following company details:
Company name: Hazardwell
Address: PO Box 58, Brindlemoor NSW 2391
Phone: 0418 264 907
Email: info@hazardwellexample.com.au
Web: www.hazardwellexample.com.au

```html
<!DOCTYPE html>
<html lang="en">
<head>
<meta charset="utf-8">
<title>Hazardwell stationery set</title>
<link href="https://fonts.googleapis.com/css2?family=Nunito:wght@800&family=Open+Sans:wght@400;600&family=Great+Vibes&display=swap" rel="stylesheet">
<style>
:root{
  --bg:#e6e3df;
  --paper:#ffffff;
  --paper-edge:#d9d9d9;
  --brand:#2f8f2a;
  --orange:#f7941d;
  --orange-light:#fdc068;
  --orange-deep:#e86f0c;
  --ink:#3a3a3a;
  --muted:#8a8a8a;
  --outline:#4a4a4a;
  --flap-dark:#1d1d1d;
  --faint:rgba(247,148,29,.12);
}
*{box-sizing:border-box;margin:0;padding:0}
html,body{width:1200px;height:562px;overflow:hidden}
body{background:var(--bg);position:relative;font-family:"Open Sans",Arial,sans-serif;color:var(--ink)}
.piece{position:absolute;background:var(--paper);box-shadow:0 2px 6px rgba(0,0,0,.25);overflow:hidden}
.wordmark{position:absolute;display:flex;align-items:center;gap:4px;font-family:"Nunito",Arial,sans-serif;font-weight:800;color:var(--brand);line-height:1;white-space:nowrap}
.wordmark .dot{width:.55em;height:.55em;background:var(--orange)}
.faint-mark{position:absolute;background:var(--faint);border-radius:12px}
.web{position:absolute;font-size:6px;color:var(--muted);white-space:nowrap}

/* warning triangle holding contact lines */
.badge{position:absolute;bottom:0}
.badge svg{display:block;width:100%;height:100%}
.badge-text{position:absolute;left:0;right:0;bottom:5px;text-align:center;font-size:4.6px;line-height:1.4;color:var(--ink);white-space:nowrap}

/* business card front */
.card-front{left:101px;top:86px;width:187px;height:106px}
.card-front .wordmark{left:10px;top:10px;font-size:16px}
.card-front .badge{left:47px;width:94px;height:62px}

/* business card back */
.card-back{left:106px;top:226px;width:184px;height:110px;background:linear-gradient(90deg,var(--orange-deep),var(--orange-light) 55%,var(--orange))}
.card-back .wordmark{left:0;right:0;top:36px;justify-content:center;font-size:22px}
.card-back .web{left:0;right:0;top:78px;text-align:center;color:#5a3a10}

/* compliments slip */
.comp-slip{left:84px;top:360px;width:214px;height:122px}
.comp-slip .wordmark{left:9px;top:10px;font-size:15px}
.comp-slip .greeting{position:absolute;right:18px;top:62px;font-family:"Great Vibes",cursive;font-size:17px;color:var(--ink);white-space:nowrap}
.comp-slip .badge{left:14px;width:96px;height:56px}
.comp-slip .web{right:10px;bottom:5px}

/* letterhead */
.letterhead{left:367px;top:70px;width:274px;height:487px}
.letterhead .wordmark{left:20px;top:20px;font-size:20px}
.letterhead .faint-mark{left:92px;top:170px;width:100px;height:100px}
.letterhead .badge{left:36px;width:100px;height:70px}
.letterhead .web{left:150px;bottom:8px}

/* envelopes */
.env-back{left:804px;top:221px;width:319px;height:110px}
.env-back .flap{position:absolute;left:0;top:0;width:100%;height:36px}
.env-back .wordmark{left:0;right:0;top:8px;justify-content:center;font-size:12px}
.env-middle{left:732px;top:278px;width:355px;height:150px}
.env-middle .band{position:absolute;left:0;top:0;width:100%;height:28px;background:linear-gradient(90deg,var(--orange-deep),var(--orange-light) 60%,var(--paper))}
.env-middle .wordmark{left:108px;top:13px;font-size:12px}
.env-front{left:773px;top:348px;width:319px;height:206px}
.env-front .wordmark{left:14px;top:12px;font-size:15px}
.env-front .faint-mark{left:190px;top:18px;width:86px;height:86px}
.env-front .badge{left:64px;width:100px;height:62px}
.env-front .web{right:16px;bottom:10px}
</style>
</head>
<body>

<section class="piece card-front" aria-label="Business card front">
  <div class="wordmark"><span>Hazardwell</span><span class="dot"></span></div>
  <div class="badge">
    <svg viewBox="0 0 94 62" preserveAspectRatio="none"><path d="M47 3 L92 62 L2 62 Z" fill="var(--orange)" stroke="var(--outline)" stroke-width="3" stroke-linejoin="round"/></svg>
    <p class="badge-text">Safety Consultant<br>0418 264 907<br>mollyfern@hazardwell<br>example.com.au</p>
  </div>
</section>

<section class="piece card-back" aria-label="Business card back">
  <div class="wordmark"><span>Hazardwell</span><span class="dot"></span></div>
  <p class="web">www.hazardwellexample.com.au</p>
</section>

<section class="piece comp-slip" aria-label="Compliments slip">
  <div class="wordmark"><span>Hazardwell</span><span class="dot"></span></div>
  <p class="greeting">With Compliments</p>
  <div class="badge">
    <svg viewBox="0 0 96 56" preserveAspectRatio="none"><path d="M48 3 L94 56 L2 56 Z" fill="var(--orange)" stroke="var(--outline)" stroke-width="3" stroke-linejoin="round"/></svg>
    <p class="badge-text">0418 264 907<br>info@hazardwell<br>example.com.au</p>
  </div>
  <p class="web">www.hazardwellexample.com.au</p>
</section>

<section class="piece letterhead" aria-label="A4 letterhead">
  <div class="wordmark"><span>Hazardwell</span><span class="dot"></span></div>
  <div class="faint-mark"></div>
  <div class="badge">
    <svg viewBox="0 0 100 70" preserveAspectRatio="none"><path d="M50 3 L98 70 L2 70 Z" fill="var(--orange)" stroke="var(--outline)" stroke-width="3" stroke-linejoin="round"/></svg>
    <p class="badge-text">PO Box 58<br>Brindlemoor NSW 2391<br>0418 264 907</p>
  </div>
  <p class="web">www.hazardwellexample.com.au</p>
</section>

<section class="piece env-back" aria-label="Envelope back with dark flap">
  <svg class="flap" viewBox="0 0 319 36" preserveAspectRatio="none"><path d="M0 0 H319 V14 L160 36 L0 14 Z" fill="var(--flap-dark)"/></svg>
  <div class="wordmark"><span>Hazardwell</span></div>
</section>

<section class="piece env-middle" aria-label="Envelope front with orange band">
  <div class="band"></div>
  <div class="wordmark"><span>Hazardwell</span><span class="dot"></span></div>
</section>

<section class="piece env-front" aria-label="White envelope front">
  <div class="wordmark"><span>Hazardwell</span><span class="dot"></span></div>
  <div class="faint-mark"></div>
  <div class="badge">
    <svg viewBox="0 0 100 62" preserveAspectRatio="none"><path d="M50 3 L98 62 L2 62 Z" fill="var(--orange)" stroke="var(--outline)" stroke-width="3" stroke-linejoin="round"/></svg>
    <p class="badge-text">PO Box 58<br>Brindlemoor NSW 2391<br>0418 264 907</p>
  </div>
  <p class="web">www.hazardwellexample.com.au</p>
</section>

</body>
</html>
```